Book Cover - For Best Selling Diet

Hi
Book cover required for a diet book being marketed to become a best seller
For best quality, image will be 2820 pixels on the shortest side and 4500 pixels on the longest side .
The book name : Bright Morning Plan
By Corinna Plett
( will add in the extra text once we see design - top and bottom subtitle )
I do not want a photo of a person on the book.
PLEASE SEE " THE 9 STEP FRAME" by Ned Galbury as an example of solid style and I also love Quiet Ledger for the font.
Branding Colours:
#F26432
#A4195C
#A7D8CC
Font that runs through our brand is : helvetica neue
This is for a book that will be marketed for #1 bestseller - So please only quality
designs that are designed in a unique style.
Thanks
Target Market(s)
Busy Working Mums, Affluent, 30+ .
Look and feel

```html
<!DOCTYPE html>
<html lang="en">
<head>
<meta charset="utf-8">
<title>Bright Morning Plan — Corinna Plett</title>
<link rel="stylesheet" href="https://fonts.googleapis.com/css2?family=Inter:wght@200;300&display=swap">
<style>
  :root {
    --slate: #a6a9b6;
    --berry: #a4195c;
    --crimson: #c42e4c;
    --coral: #f26432;
    --sand: #c9ab93;
    --ink-light: #ffffff;
    --figure-pink: #f4c8d0;
  }
  html, body {
    margin: 0;
    padding: 0;
    overflow: hidden;
    background: #ffffff;
  }
  .book-cover {
    position: relative;
    width: 752px;
    height: 1200px;
    overflow: hidden;
    background:
      radial-gradient(ellipse 60% 40% at 0% 0%, var(--slate) 0%, rgba(166,169,182,0) 100%),
      radial-gradient(ellipse 50% 32% at 100% 100%, var(--sand) 0%, rgba(201,171,147,0) 100%),
      radial-gradient(ellipse 70% 45% at 85% 12%, var(--berry) 0%, rgba(164,25,92,0) 100%),
      linear-gradient(172deg, #9c4a78 0%, var(--berry) 22%, var(--crimson) 52%, #dc4a3e 78%, var(--coral) 100%);
    font-family: "Inter", "Helvetica Neue", Arial, sans-serif;
    color: var(--ink-light);
  }
  .cover-title {
    position: absolute;
    top: 84px;
    left: 0;
    width: 100%;
    margin: 0;
    text-align: center;
    font-weight: 200;
    font-size: 136px;
    line-height: 144px;
    letter-spacing: 0;
    text-transform: uppercase;
  }
  .cover-title span { display: block; }
  .progress-figures {
    position: absolute;
    left: 28px;
    top: 662px;
    width: 712px;
    height: 280px;
  }
  .cover-author {
    position: absolute;
    left: 0;
    width: 100%;
    top: 1057px;
    margin: 0;
    text-align: center;
    font-weight: 200;
    font-size: 78px;
    line-height: 90px;
    letter-spacing: 0;
    text-transform: uppercase;
  }
</style>
</head>
<body>
  <main class="book-cover">
    <h1 class="cover-title">
      <span>Bright</span>
      <span>Morning</span>
      <span>Plan</span>
    </h1>

    <svg class="progress-figures" viewBox="0 0 712 280" role="img"
         aria-label="Row of five pale pink silhouettes of a woman walking, slimming from left to right">
      <defs>
        <radialGradient id="figure-glow" cx="0.5" cy="0.5" r="0.5">
          <stop offset="0" stop-color="var(--figure-pink)" stop-opacity="0.5"/>
          <stop offset="0.6" stop-color="var(--figure-pink)" stop-opacity="0.3"/>
          <stop offset="1" stop-color="var(--figure-pink)" stop-opacity="0"/>
        </radialGradient>
      </defs>
      <ellipse cx="356" cy="140" rx="356" ry="140" fill="url(#figure-glow)"/>
    </svg>

    <p class="cover-author">Corinna Plett</p>
  </main>
</body>
</html>
```